Blueberry Road side sign

I want a sign to put on the side of the road to advertise the that I have fresh local blueberries for sale. attatched is my company logo.
I want to use the same font that is used in my logo design.
I want "blueberries" written across the sign,
with maybe a couple of berries after the writing.

Industry/Entity Type

It Company

```html
<!DOCTYPE html>
<html lang="en">
<head>
<meta charset="utf-8">
<title>Fresh Local Blueberry – Roadside Sign</title>
<link rel="stylesheet" href="https://fonts.googleapis.com/css2?family=Pacifico&family=Quicksand:wght@700&display=swap">
<style>
  :root {
    --berry-blue: #1d4f9c;
    --berry-deep: #163f82;
    --paper: #ffffff;
    --photo-light: #eef1f5;
    --photo-berry: #8b9bb8;
    --photo-leaf: #b9cfa6;
    --shadow: rgba(20, 40, 90, 0.35);
  }
  html, body {
    margin: 0;
    padding: 0;
    overflow: hidden;
    background: var(--paper);
  }
  .sign {
    position: relative;
    width: 1200px;
    height: 600px;
    overflow: hidden;
    background: var(--paper);
  }
  .berry-photo {
    position: absolute;
    left: 430px;
    top: 0;
    width: 770px;
    height: 506px;
    background:
      radial-gradient(ellipse 200px 170px at 430px 150px, var(--photo-berry), transparent 75%),
      radial-gradient(ellipse 170px 150px at 200px 360px, var(--photo-berry), transparent 75%),
      radial-gradient(ellipse 210px 180px at 560px 370px, var(--photo-berry), transparent 75%),
      radial-gradient(ellipse 140px 110px at 240px 90px, var(--photo-leaf), transparent 75%),
      linear-gradient(90deg, var(--paper) 0%, var(--photo-light) 30%, var(--photo-light) 100%);
  }
  .headline-small {
    position: absolute;
    left: 52px;
    top: 30px;
    margin: 0;
    font-family: "Quicksand", sans-serif;
    font-weight: 700;
    font-size: 88px;
    letter-spacing: 3px;
    line-height: 1;
    color: var(--paper);
    -webkit-text-stroke: 7px var(--berry-blue);
    paint-order: stroke fill;
  }
  .headline-script {
    position: absolute;
    left: 0;
    top: 0;
    width: 1200px;
    height: 600px;
  }
  .headline-script text {
    font-family: "Pacifico", cursive;
    font-size: 300px;
  }
  .footer-band {
    position: absolute;
    left: 0;
    bottom: 0;
    width: 1200px;
    height: 94px;
    background: var(--berry-blue);
  }
  .brand {
    position: absolute;
    left: 50px;
    bottom: 24px;
    display: flex;
    align-items: center;
    gap: 14px;
    font-family: "Quicksand", sans-serif;
    font-weight: 700;
    font-size: 30px;
    color: var(--paper);
  }
  .brand-dot {
    width: 38px;
    height: 38px;
    border-radius: 50%;
    background: var(--paper);
  }
</style>
</head>
<body>
  <main class="sign">
    <div class="berry-photo" role="img" aria-label="Close-up photograph of three fresh blueberries with green leaves"></div>

    <div class="footer-band">
      <div class="brand"><span class="brand-dot"></span><span class="brand-name">Bluefield Farm</span></div>
    </div>

    <h1 class="headline-small">FRESH LOCAL</h1>

    <svg class="headline-script" viewBox="0 0 1200 600" aria-label="Blueberry">
      <defs>
        <filter id="script-shadow" x="-10%" y="-10%" width="120%" height="130%">
          <feDropShadow dx="3" dy="6" stdDeviation="5" flood-color="#142a5a" flood-opacity="0.35"/>
        </filter>
      </defs>
      <text x="48" y="420" textLength="1095" lengthAdjust="spacingAndGlyphs"
            fill="#1d4f9c" stroke="#ffffff" stroke-width="16" stroke-linejoin="round"
            paint-order="stroke fill" filter="url(#script-shadow)">Blueberry</text>
    </svg>
  </main>
</body>
</html>
```